Card design for Heating and Cooling company

this is for a heating and cooling company we recently updated our logo and need to update our cards. We attached our logo so you can incorporate it into the card. We specialize in residential and commercial furnace and air condition repairs. Have been in business since 2014.

Phone number 618.274.9031

We need the following phrases
:Repairs, Installations, and maintenance
:Quality work at reasonable prices
:residential/commercial
:Licensed &Insured
:Email Pinecresthvac47@mailbox-demo.com
Name: Tadeusz K (Ted)
Also on back side I would like my logo with wording :Thank you for your business and refferal

Industry/Entity Type

Hvac

Contact Information for Business Card

:residential/commercial
:Licensed & Insured
Name: Tadeusz K (Ted)
Number:618.274.9030

Requirements
Must have
• Blue and red colors
Nice to have
• Maybe a pic of a furnace or air conditioner

```html
<!DOCTYPE html>
<html lang="en">
<head>
<meta charset="utf-8">
<title>Pinecrest Heating &amp; Cooling – Business Card</title>
<link rel="stylesheet" href="https://fonts.googleapis.com/css2?family=Lato:wght@400;700&display=swap">
<style>
  :root {
    --backdrop: #ece8e3;
    --sky-blue: #05a8f0;
    --dusk-mauve: #8f6a78;
    --ember-red: #e63b16;
    --card-white: #f5f5f6;
    --ink: #141414;
    --text-light: #ffffff;
    --card-shadow: rgba(0, 0, 0, 0.35);
  }
  * { box-sizing: border-box; margin: 0; padding: 0; }
  html, body {
    width: 1200px;
    height: 900px;
    overflow: hidden;
    background: var(--backdrop);
    font-family: "Lato", sans-serif;
  }
  .canvas {
    position: relative;
    width: 1200px;
    height: 900px;
  }
  .card {
    position: absolute;
    width: 558px;
    height: 343px;
    box-shadow: 3px 4px 6px var(--card-shadow);
  }
  .card-front {
    left: 329px;
    top: 90px;
    background: linear-gradient(180deg, var(--sky-blue) 0%, var(--dusk-mauve) 55%, var(--ember-red) 100%);
    color: var(--text-light);
    text-align: center;
  }
  .card-back {
    left: 329px;
    top: 469px;
    width: 560px;
    background: var(--card-white);
    color: var(--ink);
    text-align: center;
  }
  .holder-name {
    position: absolute;
    top: 74px;
    left: 0;
    right: 0;
    font-size: 20px;
    font-weight: 700;
    letter-spacing: 0.2px;
  }
  .divider {
    position: absolute;
    left: 183px;
    width: 190px;
    height: 1px;
    background: var(--text-light);
  }
  .divider-top { top: 107px; }
  .divider-bottom { top: 176px; }
  .contact-list, .service-list {
    position: absolute;
    left: 0;
    right: 0;
    list-style: none;
    font-size: 16px;
    line-height: 20px;
  }
  .contact-list { top: 121px; }
  .service-list { top: 190px; }
  .brand-lockup {
    position: absolute;
    top: 150px;
    left: 0;
    right: 0;
    display: flex;
    align-items: center;
    justify-content: center;
    gap: 12px;
  }
  .brand-mark {
    width: 22px;
    height: 22px;
    border-radius: 50%;
    background: var(--sky-blue);
  }
  .brand-name {
    font-size: 26px;
    font-weight: 700;
    color: var(--ink);
    letter-spacing: 0.5px;
  }
  .thank-you {
    position: absolute;
    top: 289px;
    left: 0;
    right: 0;
    font-size: 16px;
    letter-spacing: 0.2px;
    text-transform: uppercase;
  }
</style>
</head>
<body>
<main class="canvas">
  <section class="card card-front" aria-label="Card front">
    <h1 class="holder-name">TADEUSZ K (TED)</h1>
    <div class="divider divider-top"></div>
    <ul class="contact-list">
      <li>618.274.9030</li>
      <li>Pinecresthvac47@mailbox-demo.com</li>
    </ul>
    <div class="divider divider-bottom"></div>
    <ul class="service-list">
      <li>Repairs, Installations, and maintenance</li>
      <li>Residential/commercial</li>
      <li>Quality work at reasonable prices</li>
      <li>Licensed &amp; Insured</li>
    </ul>
  </section>

  <section class="card card-back" aria-label="Card back">
    <div class="brand-lockup">
      <span class="brand-mark"></span>
      <span class="brand-name">PINECREST HEATING &amp; COOLING</span>
    </div>
    <p class="thank-you">Thank you for your business and refferal</p>
  </section>
</main>
</body>
</html>
```